home theater/ flat panel TV installation/ computer networking

single page flyer front and back, I am paying for adress labels so it should be 8 1/2" x 11" tri-fold with a place for the labels to go and be easy to mail.

Brightline Media

Charlotte NC 28917

http://www.brightlinemedianc.example/

call today for your no cost consultation  704-418-2263

Call today for your no cost consultation!    704-418-2263  Brightline Media

If your new home came with a finished basement, or you are

finishing it yourself, consider making part of it into a great home

theater. Why not add a fantastic High Definition projector and 100”

screen to your lovely new home? Experience satellite and cable TV,

video games, and of course, movies like you have never seen or

heard before. The cost of the system is probably a lot less than you

think. Finally, we install everything and provide a single programmed

remote to operate the entire system, easily! Already have a High

Definition TV? Let us integrate it with speakers, programmable

remotes, even a popcorn machine! Free consultations at your

request.

professional home theater designer and network cable installations in Texas

regular size.  I am picturing 8 1/2" x 11"  tri-fold.   I have never had a flyer before and am willing to accept different sizes.   

 

Target Market(s)

These will be sent to new home owners already looking for these services. I am a small company trying to say "we are the best".

These are the services we sell... (feel free to High-light or bullet)

-Home Theater
-High Definition TV
-Surround Sound
-All-in-One remotes
-Computer Networks
-Liscenced Electrician
-Lighting control

Industry/Entity Type

Computer

Requirements
Must have
• most of these photos. I am willing to pay for something better if available.  maybe a family or something.

• customer testimonial (should be italisized)

• "Brightline Media showed up on time, cleaned up after themselves, they we great!"

• "...we left the key under the mat, when we got home the TV was on the wall..."
Nice to have
• sonic wave from business card.eps file
• a few more photos

```html
<!DOCTYPE html>
<html lang="en">
<head>
<meta charset="utf-8">
<title>Brightline Media – Tri-fold Mailer</title>
<link rel="stylesheet" href="https://fonts.googleapis.com/css2?family=Questrial&family=Crimson+Text:ital,wght@0,600;1,400&display=swap">
<style>
  :root{
    --page:#ffffff;
    --sky-light:#eef5fb;
    --sky:#d9e8f4;
    --steel:#5f8cab;
    --steel-dark:#4d7999;
    --brand-blue:#3a86c4;
    --ink:#3f4347;
    --ink-soft:#5a5f64;
    --white:#ffffff;
    --photo-grey-a:#3a3a3a;
    --photo-grey-b:#9a9a9a;
  }
  *{box-sizing:border-box;margin:0;padding:0}
  html,body{width:1200px;height:1184px;overflow:hidden;background:var(--page)}
  body{position:relative;font-family:"Questrial",sans-serif;color:var(--ink)}

  .panel{position:absolute;left:230px;width:740px;height:572px;overflow:hidden;
    background:linear-gradient(135deg,var(--sky-light) 0%,var(--sky) 55%,var(--sky-light) 100%);
    box-shadow:0 2px 6px rgba(0,0,0,.18)}
  .panel--outside{top:20px}
  .panel--inside{top:592px}

  .photo{position:absolute}

  /* outside */
  .outside__photo{left:0;top:0;width:245px;height:572px;
    background:linear-gradient(160deg,var(--photo-grey-a),var(--photo-grey-b) 45%,var(--photo-grey-a))}
  .stamp-box{position:absolute;left:440px;top:20px;width:37px;height:37px;background:var(--white)}
  .label-box{position:absolute;left:274px;top:287px;width:191px;height:118px;background:var(--white)}
  .brand{color:var(--brand-blue);font-family:"Questrial",sans-serif;white-space:nowrap}
  .outside__brand{position:absolute;left:530px;top:180px;font-size:26px;letter-spacing:.5px}
  .return-block{position:absolute;left:255px;top:436px;width:246px;text-align:center}
  .return-block .brand{font-size:19px;display:block;margin-bottom:10px}
  .return-block .city{font-size:11px;color:var(--ink)}
  .return-block .url{font-size:9px;color:var(--ink-soft);margin-top:3px}
  .return-block .cta{font-size:11.5px;margin-top:8px}
  .return-block .phone{font-size:19px;margin-top:6px;letter-spacing:.5px}

  /* inside */
  .inside__headline{position:absolute;left:29px;top:22px;font-size:12.5px;letter-spacing:.6px;color:var(--brand-blue);text-transform:uppercase}
  .intro{position:absolute;left:22px;width:226px;text-align:center;font-size:11px;line-height:1.55;color:var(--ink)}
  .intro--first{top:86px}
  .intro--second{top:250px}
  .callout{position:absolute;background:var(--steel);color:var(--white);text-align:center;text-transform:uppercase;
    font-size:10px;line-height:1.55;letter-spacing:.3px;display:flex;align-items:center;justify-content:center;padding:0 12px}
  .callout--projector{left:12px;top:157px;width:245px;height:76px}
  .callout--hdtv{left:493px;top:262px;width:237px;height:40px}
  .remotes{left:37px;top:394px;width:169px;height:143px;
    background:radial-gradient(ellipse at center,#8aa2b8 0%,#c8d6e2 55%,rgba(217,232,244,0) 75%)}

  .services{position:absolute;left:277px;top:51px;width:183px;height:199px;background:var(--steel);color:var(--white);padding:14px 16px}
  .services h2{font-weight:400;font-size:13px;letter-spacing:.6px;text-transform:uppercase;margin-bottom:8px}
  .services ul{list-style:none}
  .services li{font-size:11px;line-height:2.05}
  .services li::before{content:"•";margin-right:6px}

  .photo--fireplace{left:561px;top:0;width:179px;height:128px;background:linear-gradient(160deg,#d6c39c,#8d6a43)}
  .photo--media-wall{left:463px;top:132px;width:95px;height:110px;background:linear-gradient(160deg,#5a3d2a,#9b7a5a)}
  .photo--living{left:561px;top:132px;width:179px;height:110px;background:linear-gradient(160deg,#7a5a3e,#cdb394)}
  .photo--theater{left:274px;top:275px;width:186px;height:156px;background:linear-gradient(170deg,#6b4a33,#2a1e18)}

  .testimonial{position:absolute;left:274px;top:445px;width:200px;font-family:"Crimson Text",serif}
  .testimonial h3{font-weight:600;font-size:11.5px;color:var(--steel-dark);margin-bottom:7px}
  .testimonial p{font-style:italic;font-size:10.5px;line-height:1.4;color:var(--ink-soft);margin-bottom:9px}

  .upgrade{position:absolute;left:493px;top:320px;width:237px;text-align:center;font-size:11px;line-height:1.6}

  .consult{position:absolute;left:493px;top:394px;width:237px;height:155px;border:1px solid #8a9aa8;padding:14px 16px}
  .consult h2{font-weight:400;font-size:13px;letter-spacing:.5px;text-transform:uppercase;line-height:1.35;color:var(--ink)}
  .consult .url{font-size:10px;color:var(--ink-soft);margin-top:10px}
  .consult .cta{font-size:11px;line-height:1.45;margin-top:12px;color:var(--ink-soft)}
  .consult .cta strong{font-weight:400;font-size:15px;color:var(--ink)}
</style>
</head>
<body>

<section class="panel panel--outside" aria-label="Outside of tri-fold mailer">
  <div class="photo outside__photo" role="img" aria-label="Black and white photo of a wall of flat-panel televisions"></div>
  <div class="stamp-box" aria-label="Postage area"></div>
  <div class="label-box" aria-label="Mailing label area"></div>
  <div class="brand outside__brand">Brightline Media</div>
  <div class="return-block">
    <span class="brand">Brightline Media</span>
    <p class="city">Charlotte NC 28917</p>
    <p class="url">www.brightlinemedianc.example</p>
    <p class="cta">Call today for your no cost consultation</p>
    <p class="phone">704-418-2263</p>
  </div>
</section>

<section class="panel panel--inside" aria-label="Inside of tri-fold mailer">
  <h1 class="inside__headline">Experience, professional and reliable.</h1>

  <p class="intro intro--first">If your new home came with a finished basement, or you are finishing it yourself, consider making part of it into a great home theater.</p>
  <div class="callout callout--projector">Why not add a fantastic high definition projector and 100" screen to your lovely new home?</div>
  <p class="intro intro--second">Experience satellite and cable TV, video games, and of course, movies like you have never seen or heard before. The cost of the system is probably a lot less than you think. Finally, we install everything and provide a single programmed remote to operate the entire system, easily!</p>
  <div class="photo remotes" role="img" aria-label="Photo of three programmable universal remotes"></div>

  <div class="services">
    <h2>Services we sell</h2>
    <ul>
      <li>Home Theater</li>
      <li>High Definition TV</li>
      <li>Surround Sound</li>
      <li>All-in-One remotes</li>
      <li>Computer Networks</li>
      <li>Licensed Electrician</li>
      <li>Lighting control</li>
    </ul>
  </div>

  <div class="photo photo--fireplace" role="img" aria-label="Photo of a flat-panel TV mounted above a fireplace"></div>
  <div class="photo photo--media-wall" role="img" aria-label="Photo of a TV set into a wooden media wall"></div>
  <div class="photo photo--living" role="img" aria-label="Photo of a living room with a wall-mounted screen"></div>
  <div class="photo photo--theater" role="img" aria-label="Photo of a home theater with leather recliners"></div>

  <div class="testimonial">
    <h3>Customer Testimonial</h3>
    <p>"Brightline Media showed up on time, cleaned up after themselves, they were great!"</p>
    <p>"...we left the key under the mat, when we got home the TV was on the wall..."</p>
  </div>

  <div class="callout callout--hdtv">Already have a high definition TV?</div>
  <p class="upgrade">Let us integrate it with speakers, programmable remotes, even a popcorn machine!</p>

  <div class="consult">
    <h2>Free consultations<br>at your request.</h2>
    <p class="url">www.brightlinemedianc.example</p>
    <p class="cta">Call today for your no cost consultation at <strong>704-418-2263</strong></p>
  </div>
</section>

</body>
</html>
```